Visitenkarten-Design für Erfindung & Entwicklung von Produkten für Körper, Geist und Seele
Zielgruppe
Erfindung und Entwicklung von Produkten für Körper Geist und Seele
Als grosser Überbegriff Produkte zur Regenration und Wohlbefinden sowie Bewusstseins Förderung
' Beispiel ' www. o-senva.ch
Zielgruppe Jedermann und Jedefrau die Ihr Bewusstein für Ihre Gesundheit und Heilung auf allen Ebenen vertiefen möchte ....
Aufgabenstellung
Das Logo ist Entwickelt in einem Entwurfsstadium kleine Verbesserungsvorschläge wären möglich
Vorallem geht es um das Layout und der sauberen Daten Erfassung
sowie die Gestaltung der Visitenkarte

```html
<!DOCTYPE html>
<html lang="de">
<head>
<meta charset="utf-8">
<title>Velmora – Visitenkarte</title>
<link rel="stylesheet" href="https://fonts.googleapis.com/css2?family=Ubuntu:wght@400;500;700&display=swap">
<style>
  :root {
    --bg: #e6e6e6;
    --card-dark: #050505;
    --card-light: #ffffff;
    --green: #4f7a12;
    --green-mark: #5e8f1a;
    --gold: #a99a1c;
    --ink: #1a1a1a;
    --white: #ffffff;
  }
  * { box-sizing: border-box; margin: 0; padding: 0; }
  html, body { width: 1200px; height: 1059px; overflow: hidden; }
  body {
    background: var(--bg);
    font-family: "Ubuntu", sans-serif;
    display: flex;
    flex-direction: column;
    align-items: center;
    justify-content: center;
    gap: 50px;
  }
  .card {
    position: relative;
    width: 800px;
    height: 457px;
    overflow: hidden;
    box-shadow: 0 10px 30px rgba(0,0,0,.18);
  }

  /* brand block */
  .brand { position: absolute; display: flex; flex-direction: column; gap: 10px; }
  .brand-name {
    display: flex; align-items: center; gap: 16px;
    font-family: "Ubuntu", sans-serif;
    font-weight: 500;
    font-size: 44px;
    line-height: 1;
  }
  .brand-square { width: 20px; height: 20px; background: var(--green-mark); flex: none; }
  .tagline {
    font-family: "Ubuntu", sans-serif;
    font-weight: 400;
    color: var(--gold);
    font-size: 18px;
    text-transform: uppercase;
    letter-spacing: 3px;
    padding-left: 36px;
  }

  /* front */
  .card-front { background: var(--card-dark); }
  .card-front .brand { left: 0; right: 0; top: 160px; align-items: center; }
  .card-front .brand-name { color: var(--white); }
  .card-front .tagline { padding-left: 0; }
  .card-front .url {
    position: absolute; left: 0; right: 0; bottom: 72px;
    text-align: center; color: var(--white); font-size: 20px; letter-spacing: .5px;
  }

  /* back */
  .card-back { background: var(--card-light); }
  .card-back .brand { left: 60px; top: 128px; }
  .card-back .brand-name { color: var(--ink); font-size: 38px; }
  .card-back .brand-square { width: 18px; height: 18px; }
  .card-back .tagline { font-size: 15px; padding-left: 34px; }
  .divider {
    position: absolute; left: 452px; top: 92px;
    width: 2px; height: 132px; background: var(--green);
  }
  .contact { position: absolute; left: 478px; top: 92px; }
  .person { color: var(--green); font-weight: 700; font-size: 27px; margin-bottom: 12px; }
  .contact-list { list-style: none; }
  .contact-list li {
    display: flex; align-items: center; gap: 12px;
    font-size: 19px; color: var(--ink); line-height: 30px;
  }
  .contact-list svg { width: 16px; height: 16px; flex: none; }
  .address {
    position: absolute; left: 60px; bottom: 96px;
    font-size: 23px; color: var(--ink);
  }
  .address .dot { color: var(--green); margin: 0 6px; }
  .gold-rule { position: absolute; left: 0; right: 0; bottom: 58px; height: 5px; background: var(--gold); }
  .base-band { position: absolute; left: 0; right: 0; bottom: 0; height: 52px; background: var(--card-dark); }
</style>
</head>
<body>

  <section class="card card-front">
    <div class="brand">
      <div class="brand-name"><span class="brand-square"></span>Velmora</div>
      <div class="tagline">klar gestalten</div>
    </div>
    <div class="url">www.velmora.ch</div>
  </section>

  <section class="card card-back">
    <div class="brand">
      <div class="brand-name"><span class="brand-square"></span>Velmora</div>
      <div class="tagline">klar gestalten</div>
    </div>
    <div class="divider"></div>
    <div class="contact">
      <div class="person">Kolu Trisvend</div>
      <ul class="contact-list">
        <li>
          <svg viewBox="0 0 16 16"><rect x="4" y="1" width="8" height="14" rx="1.5" fill="none" stroke="#4f7a12" stroke-width="1.5"/><circle cx="8" cy="12.5" r=".9" fill="#4f7a12"/></svg>
          079 000 12 34
        </li>
        <li>
          <svg viewBox="0 0 16 16"><rect x="1" y="3" width="14" height="10" fill="#4f7a12"/><path d="M1 3 L8 9 L15 3" fill="none" stroke="#fff" stroke-width="1.3"/></svg>
          kolu.trisvend@velmora.ch
        </li>
        <li>
          <svg viewBox="0 0 16 16"><circle cx="8" cy="8" r="7" fill="#4f7a12"/><path d="M1.5 8 H14.5 M8 1 C5 5 5 11 8 15 M8 1 C11 5 11 11 8 15" fill="none" stroke="#fff" stroke-width="1"/></svg>
          www.velmora.ch
        </li>
      </ul>
    </div>
    <div class="address">Velmora<span class="dot">•</span>Lindenrain 14<span class="dot">•</span>8000 Musterdorf</div>
    <div class="gold-rule"></div>
    <div class="base-band"></div>
  </section>

</body>
</html>
```